Create branded design templates/backgrounds for social media based on UK property investing company

I'd like Instagram, Facebook and Linkedin backgrounds/templates to add text to, based on my logo design and business of UK holiday let investing. Ideally I'd have some base designs for me to approve, then engage with the winning designer further to create about 50 different templates. I looking for a mixture of templates with the logo and using logo colours, others of internal holiday let photos including logos and a few of my photo imposed on the front of them.

Target Market(s)

Middle aged adults

Industry/Entity Type

Holiday let properties

Requirements
Must have
• a distinct brand look that can be replicated

```html
<!DOCTYPE html>
<html lang="en">
<head>
<meta charset="utf-8">
<title>Instagram post template set</title>
<link href="https://fonts.googleapis.com/css2?family=Open+Sans:wght@400;600;700&display=swap" rel="stylesheet">
<style>
  :root {
    --brand-blue: #0a84d6;
    --brand-green: #4fa80f;
    --brand-yellow: #f4d92b;
    --brand-navy: #0c3d73;
    --white: #ffffff;
    --page: #ffffff;
    --caption: #111111;
  }
  html, body {
    margin: 0;
    padding: 0;
    width: 1200px;
    height: 675px;
    overflow: hidden;
    background: var(--page);
    font-family: "Open Sans", sans-serif;
  }
  .board { position: relative; width: 1200px; height: 675px; }
  .post {
    position: absolute;
    width: 249px;
    height: 249px;
    box-shadow: 0 3px 6px rgba(0,0,0,0.18);
    overflow: hidden;
  }
  .post svg { display: block; width: 249px; height: 249px; }
  .post text { font-family: "Open Sans", sans-serif; }
  .row-top { top: 77px; }
  .row-bottom { top: 349px; }
  .col-1 { left: 67px; }
  .col-2 { left: 326px; }
  .col-3 { left: 625px; }
  .col-4 { left: 883px; }
  .caption {
    position: absolute;
    left: 67px;
    top: 620px;
    margin: 0;
    font-size: 15px;
    font-weight: 400;
    color: var(--caption);
  }
  .brand-name { font-weight: 600; fill: var(--white); font-size: 12px; }
  .callout-copy { font-weight: 600; fill: var(--white); }
  .callout-copy.navy { fill: var(--brand-navy); }
  .callout-copy.blue { fill: var(--brand-blue); }
</style>
</head>
<body>
<div class="board">
  <svg width="0" height="0" style="position:absolute">
    <defs>
      <linearGradient id="street-sky" x1="0" y1="0" x2="0" y2="1">
        <stop offset="0" stop-color="#5d9de0"/>
        <stop offset="0.22" stop-color="#a9c4e0"/>
        <stop offset="0.32" stop-color="#a8653c"/>
        <stop offset="0.55" stop-color="#c88a4f"/>
        <stop offset="0.8" stop-color="#b37a4a"/>
        <stop offset="1" stop-color="#4a4746"/>
      </linearGradient>
      <linearGradient id="street-side" x1="0" y1="0" x2="1" y2="0">
        <stop offset="0" stop-color="#2a2a30" stop-opacity="0.35"/>
        <stop offset="0.5" stop-color="#000" stop-opacity="0"/>
        <stop offset="1" stop-color="#f3ece4" stop-opacity="0.25"/>
      </linearGradient>
      <radialGradient id="keys-warm" cx="0.45" cy="0.45" r="0.75">
        <stop offset="0" stop-color="#eed8cc"/>
        <stop offset="0.45" stop-color="#e2ad93"/>
        <stop offset="1" stop-color="#c88f78"/>
      </radialGradient>
      <radialGradient id="man-keys" cx="0.6" cy="0.45" r="0.8">
        <stop offset="0" stop-color="#d5b39c"/>
        <stop offset="0.55" stop-color="#b99a86"/>
        <stop offset="1" stop-color="#e6e2dd"/>
      </radialGradient>
      <radialGradient id="couple-warm" cx="0.45" cy="0.5" r="0.8">
        <stop offset="0" stop-color="#e3c3ae"/>
        <stop offset="0.5" stop-color="#b08970"/>
        <stop offset="1" stop-color="#ece7e1"/>
      </radialGradient>
      <linearGradient id="wall-dusk" x1="0" y1="0" x2="1" y2="1">
        <stop offset="0" stop-color="#7a5240"/>
        <stop offset="0.45" stop-color="#4c3429"/>
        <stop offset="0.75" stop-color="#3a3a46"/>
        <stop offset="1" stop-color="#1f2634"/>
      </linearGradient>
      <linearGradient id="portrait-tone" x1="0" y1="0" x2="0" y2="1">
        <stop offset="0" stop-color="#dcb19d" stop-opacity="0.9"/>
        <stop offset="0.6" stop-color="#c9a08c" stop-opacity="0.9"/>
        <stop offset="1" stop-color="#5f625e"/>
      </linearGradient>
      <linearGradient id="portrait-fade" x1="0" y1="0" x2="0" y2="1">
        <stop offset="0" stop-color="#f4d92b" stop-opacity="0"/>
        <stop offset="0.35" stop-color="#e4b99f" stop-opacity="0.55"/>
        <stop offset="0.75" stop-color="#c39a88" stop-opacity="0.85"/>
        <stop offset="1" stop-color="#66665f"/>
      </linearGradient>
      <clipPath id="house-frame">
        <polygon points="148,27 274,92 274,267 119,267 26,317 26,95"/>
      </clipPath>
    </defs>
  </svg>

  <!-- Post 1 -->
  <div class="post row-top col-1">
    <svg viewBox="0 0 398 398">
      <g role="img" aria-label="Photo of a row of red-brick terraced houses under a blue sky">
        <rect width="398" height="398" fill="url(#street-sky)"/>
        <rect width="398" height="398" fill="url(#street-side)"/>
      </g>
      <polygon points="398,352 398,398 332,398" fill="var(--brand-blue)"/>
    </svg>
  </div>

  <!-- Post 2 -->
  <div class="post row-top col-2">
    <svg viewBox="0 0 398 398">
      <rect width="398" height="398" fill="var(--brand-blue)"/>
      <polygon points="148,27 274,92 274,267 119,267 26,317 26,95" fill="url(#keys-warm)" role="img" aria-label="Photo of a couple holding up house keys with a small house keyring"/>
      <polygon points="299,202 372,242 372,342 264,342 229,369 229,242" fill="var(--brand-green)"/>
      <text class="callout-copy" font-size="13">
        <tspan x="244" y="260">We have just</tspan>
        <tspan x="244" y="276">bought this</tspan>
        <tspan x="244" y="292">property today,</tspan>
        <tspan x="244" y="308">would you like to</tspan>
        <tspan x="244" y="324">invest?</tspan>
      </text>
      <rect x="27" y="356" width="12" height="12" fill="var(--white)"/>
      <text class="brand-name" x="45" y="367">Keystone Lets</text>
    </svg>
  </div>

  <!-- Post 3 -->
  <div class="post row-top col-3">
    <svg viewBox="0 0 398 398">
      <rect width="398" height="398" fill="url(#man-keys)" role="img" aria-label="Photo of a man holding up a bunch of keys"/>
      <polygon points="198,52 326,125 326,297 130,297 73,344 73,125" fill="none" stroke="var(--white)" stroke-width="8"/>
      <polygon points="89,25 152,62 152,148 60,148 26,174 26,62" fill="var(--brand-blue)"/>
      <text class="callout-copy" font-size="10.5">
        <tspan x="40" y="75">We have just</tspan>
        <tspan x="40" y="88">bought this</tspan>
        <tspan x="40" y="101">property today,</tspan>
        <tspan x="40" y="114">would you like to</tspan>
        <tspan x="40" y="127">invest?</tspan>
      </text>
      <rect x="259" y="356" width="12" height="12" fill="var(--white)"/>
      <text class="brand-name" x="277" y="367">Keystone Lets</text>
    </svg>
  </div>

  <!-- Post 4 -->
  <div class="post row-top col-4">
    <svg viewBox="0 0 398 398">
      <rect width="398" height="398" fill="url(#couple-warm)" role="img" aria-label="Photo of a smiling couple looking at a new home"/>
      <polygon points="300,202 373,242 373,342 264,342 229,369 229,242" fill="var(--brand-green)"/>
      <text class="callout-copy" font-size="10">
        <tspan x="244" y="256">Lorem ipsum dolor sit</tspan>
        <tspan x="244" y="268">amet, consectetur</tspan>
        <tspan x="244" y="280">adipiscing elit, sed do</tspan>
        <tspan x="244" y="292">eiusmod tempor</tspan>
        <tspan x="244" y="304">incididunt ut labore et</tspan>
        <tspan x="244" y="316">dolore magna aliqua.</tspan>
      </text>
      <rect x="27" y="356" width="12" height="12" fill="var(--white)"/>
      <text class="brand-name" x="45" y="367">Keystone Lets</text>
    </svg>
  </div>

  <!-- Post 5 -->
  <div class="post row-bottom col-1">
    <svg viewBox="0 0 398 398">
      <g role="img" aria-label="Photo of a row of red-brick terraced houses">
        <rect width="398" height="398" fill="url(#street-sky)"/>
        <rect width="398" height="398" fill="url(#street-side)"/>
      </g>
      <polygon points="0,290 90,238 174,286 174,398 0,398" fill="var(--brand-blue)"/>
      <polygon points="0,290 90,238 174,286 174,398 0,398" fill="url(#portrait-tone)" opacity="0.85" role="img" aria-label="Portrait photo of the company founder"/>
      <polygon points="302,26 373,66 373,167 260,167 229,193 229,66" fill="var(--white)"/>
      <text class="callout-copy blue" font-size="13">
        <tspan x="244" y="85">We have just</tspan>
        <tspan x="244" y="101">bought this</tspan>
        <tspan x="244" y="117">property today,</tspan>
        <tspan x="244" y="133">would you like to</tspan>
        <tspan x="244" y="149">invest?</tspan>
      </text>
      <rect x="27" y="38" width="12" height="12" fill="var(--white)"/>
      <text class="brand-name" x="45" y="49">Keystone Lets</text>
    </svg>
  </div>

  <!-- Post 6 -->
  <div class="post row-bottom col-2">
    <svg viewBox="0 0 398 398">
      <rect width="398" height="398" fill="url(#wall-dusk)" role="img" aria-label="Photo of an old brick building with a painted sign and a corner shop"/>
      <polygon points="292,154 384,204 384,334 240,334 199,371 199,204" fill="var(--white)"/>
      <text class="callout-copy navy" font-size="13">
        <tspan x="220" y="226">Lorem ipsum dolor sit</tspan>
        <tspan x="220" y="241">amet, consectetur</tspan>
        <tspan x="220" y="256">adipiscing elit, sed do</tspan>
        <tspan x="220" y="271">eiusmod tempor</tspan>
        <tspan x="220" y="286">incididunt ut labore et</tspan>
        <tspan x="220" y="301">dolore magna aliqua.</tspan>
      </text>
    </svg>
  </div>

  <!-- Post 7 -->
  <div class="post row-bottom col-3">
    <svg viewBox="0 0 398 398">
      <rect width="398" height="398" fill="var(--brand-blue)"/>
      <polygon points="148,27 274,92 274,267 119,267 26,317 26,95" fill="url(#keys-warm)" role="img" aria-label="Photo of a couple holding up house keys with a small house keyring"/>
      <polygon points="299,202 372,242 372,342 264,342 229,369 229,242" fill="var(--brand-green)"/>
      <text class="callout-copy" font-size="13">
        <tspan x="244" y="260">We have just</tspan>
        <tspan x="244" y="276">bought this</tspan>
        <tspan x="244" y="292">property today,</tspan>
        <tspan x="244" y="308">would you like to</tspan>
        <tspan x="244" y="324">invest?</tspan>
      </text>
      <rect x="27" y="356" width="12" height="12" fill="var(--white)"/>
      <text class="brand-name" x="45" y="367">Keystone Lets</text>
    </svg>
  </div>

  <!-- Post 8 -->
  <div class="post row-bottom col-4">
    <svg viewBox="0 0 398 398">
      <rect width="398" height="398" fill="var(--brand-blue)"/>
      <polygon points="148,27 274,92 274,267 119,267 26,317 26,95" fill="var(--brand-yellow)"/>
      <rect x="26" y="27" width="248" height="290" fill="url(#portrait-fade)" clip-path="url(#house-frame)" role="img" aria-label="Portrait photo of the company founder"/>
      <polygon points="299,202 372,242 372,342 264,342 229,369 229,242" fill="var(--brand-green)"/>
      <text class="callout-copy" font-size="10">
        <tspan x="244" y="256">Lorem ipsum dolor sit</tspan>
        <tspan x="244" y="268">amet, consectetur</tspan>
        <tspan x="244" y="280">adipiscing elit, sed do</tspan>
        <tspan x="244" y="292">eiusmod tempor</tspan>
        <tspan x="244" y="304">incididunt ut labore et</tspan>
        <tspan x="244" y="316">dolore magna aliqua.</tspan>
      </text>
      <rect x="27" y="356" width="12" height="12" fill="var(--white)"/>
      <text class="brand-name" x="45" y="367">Keystone Lets</text>
    </svg>
  </div>

  <p class="caption">instagram post template example</p>
</div>
</body>
</html>
```